Design Creative Banner or Gif Ads. 3 Designs To Be Selected

Come up with some creative banner ads for stonewell.co.nz

*At least 3 different winning banners will be chosen*

Please provide banner ads / gif ads in common google ads / website banner formats.

They can be gif or static but must stand out while still maintaining clear clean text and visuals, with a premium professional feel (please avoid clip art or anything that gives a cheap message).

Please keep in mind that these will likely be small ads so text needs to be large and if there's there a lot of text then use multiple frames/ pages as submit as a gif.

Style
Minimal & clean lines
Architectural or realistic images
Avoid cartoon styles, clipart, or anything that looks cheap

Font
Nexa or Montserrat or similar

Tone
Premium, serious, trustworthy — fits new builds

Colours
Option 1: Deep Navy (trust & quality) & lighter blues and warm grey
Option 2: Open to bright colours to help the ads stand out, such as (but not limited to) bright pink with black, yellow, fluorescent green, provided the messaging is still done professionally.
Our logo is attached (Stone Well Logo)

Display Sizes
Ad specs for file sizes should be file formats like JPEG, GIF, and PNG, with animations limited to a max of 30 seconds or less.
We will need several different ad sizes provided for each of the 3 selected winning designs.

• Medium Rectangle: 300 × 250 pixels
• Leaderboard: 728 × 90 pixels
• Desktop Banner ad image: (640x360 pixels)
• Desktop Banner ad image 2: (300x600 pixels)
• Possibly one or two other sizes

Flexibility to be creative
The ad text, words, upper/lower case, layout, colour, theme, and images can be adjusted to how you think it will look best. The follow example ads are just examples of what we are after but we are keen to see what you can create.

Recommendations at this point:
1. Avoid text heavy
2. Looking for more Gif ads
3. Imaging: if possible use real stock photo's rather than AI

Themes:

1
Building Soon? Start Here
Free Build Planning Pack:
✓ Build Cost Calculator
✓ Hidden Cost Checklist
✓ Builder Comparison Guide
Build With Confidence
Download Free

2
Before You Choose A Builder
Compare Price, Scope, Risk & Value
Avoid Costly Mistakes
Choose The Right Builder With Confidence
Download The Free Guide

3
Planning A New Build?
Avoid These Common Mistakes:
✗ Hidden Exclusions
✗ Missing Scope
✗ Unrealistic Allowances
✗ Budget Blowouts
Download The Free Guide

4
Before You Buy Land
Know what it could cost to build.
Avoid Costly Building Mistakes
Download Our Free Guides

5
Know Your Build Budget?
• Free Build Cost Calculator
• Hidden Cost Checklist
• Build Planning Tools
Calculate Costs (Download)

Target Market(s)

Landowners looking to build

Industry/Entity Type

Building

Font styles to use
Other font styles liked:
• Nexa or Montserrat or similar

Requirements
Should not have
• Avoid cartoon styles, clipart, or anything that looks cheap

```html
<!DOCTYPE html>
<html lang="en">
<head>
<meta charset="utf-8">
<title>Stone Well – Display Banners</title>
<link rel="stylesheet" href="https://fonts.googleapis.com/css2?family=Montserrat:wght@400;600;700;800&display=swap">
<style>
  :root{
    --board:#d1d2d4;
    --navy:#0f2c47;
    --navy-deep:#0a2238;
    --navy-light:#163a5a;
    --sky:#29a0cc;
    --button:#1d6f9f;
    --white:#ffffff;
    --label:#1a1a1a;
    --photo-light:#e6e6e4;
    --photo-mid:#9a9b9a;
    --photo-warm:#b58a52;
  }
  *{box-sizing:border-box;margin:0;padding:0}
  html,body{width:1200px;height:1060px;overflow:hidden;background:var(--board)}
  body{position:relative;font-family:"Montserrat",sans-serif;color:var(--white)}
  .size-label{position:absolute;font-family:"Times New Roman",serif;font-size:18px;color:var(--label);line-height:1}
  .size-label.tall{left:600px;top:14px}
  .size-label.rect{left:458px;top:672px}

  .banner{position:absolute;overflow:hidden;
    background:
      linear-gradient(135deg,var(--navy-light) 0%,var(--navy) 45%,var(--navy-deep) 100%);}
  .banner > *{position:absolute;line-height:1;white-space:nowrap}
  .rect-ad{left:65px;top:266px;width:485px;height:403px}
  .tall-ad{left:598px;top:40px;width:485px;height:968px}

  .brand-mark{background:var(--sky)}
  .brand-name{font-weight:600;color:var(--white)}
  .headline{font-weight:700;color:var(--sky)}
  .subhead{font-weight:800;color:var(--white)}
  .pack-title{font-weight:400}
  .pack-item{font-weight:400}
  .item-icon{stroke:var(--sky);fill:none;stroke-width:1.6;stroke-linecap:round;stroke-linejoin:round}
  .tagline{font-weight:400;text-align:center}
  .cta{display:flex;align-items:center;justify-content:center;background:var(--button);
       border:2px solid var(--white);border-radius:5px;font-weight:400;color:var(--white)}
  .photo{background:
      linear-gradient(180deg,rgba(15,44,71,0) 0%,rgba(15,44,71,0) 30%,rgba(15,44,71,.0) 100%),
      linear-gradient(100deg,var(--photo-light) 0%,var(--photo-mid) 45%,var(--photo-warm) 75%,var(--photo-light) 100%);
      -webkit-mask-image:linear-gradient(180deg,transparent 0%,#000 25%);
      mask-image:linear-gradient(180deg,transparent 0%,#000 25%);}
  .accent-bar{background:var(--sky)}

  /* 300x250 */
  .rect-ad .brand-mark{left:39px;top:22px;width:26px;height:26px}
  .rect-ad .brand-name{left:73px;top:25px;font-size:17px}
  .rect-ad .headline{left:38px;top:91px;font-size:37px}
  .rect-ad .subhead{left:38px;top:135px;font-size:26px}
  .rect-ad .pack-title{left:36px;top:176px;font-size:17px}
  .rect-ad .pack-item{left:69px;font-size:16px;line-height:21px}
  .rect-ad .item-icon{left:38px;width:16px;height:16px}
  .rect-ad .tagline{left:74px;top:319px;width:149px;font-size:13px}
  .rect-ad .cta{left:74px;top:340px;width:149px;height:31px;font-size:15px}
  .rect-ad .photo{left:279px;top:150px;width:206px;height:253px}
  .rect-ad .accent-bar{left:0;bottom:0;width:485px;height:9px}

  /* 300x600 */
  .tall-ad .brand-mark{left:46px;top:45px;width:44px;height:44px}
  .tall-ad .brand-name{left:115px;top:58px;font-size:28px}
  .tall-ad .headline{left:42px;top:153px;font-size:48px}
  .tall-ad .subhead{left:42px;top:207px;font-size:34px}
  .tall-ad .pack-title{left:40px;top:315px;font-size:26px}
  .tall-ad .pack-item{left:92px;font-size:25px;line-height:34px}
  .tall-ad .item-icon{left:42px;width:26px;height:26px}
  .tall-ad .tagline{left:117px;top:569px;width:253px;font-size:21px}
  .tall-ad .cta{left:117px;top:604px;width:253px;height:52px;font-size:26px}
  .tall-ad .photo{left:0;top:612px;width:485px;height:356px}
</style>
</head>
<body>
  <div class="size-label tall">300X600px</div>
  <div class="size-label rect">300X250px</div>

  <section class="banner rect-ad" aria-label="Medium rectangle banner">
    <div class="photo" role="img" aria-label="Photo of a new two-storey house under construction with scaffolding and timber roof framing"></div>
    <div class="brand-mark"></div>
    <div class="brand-name">Stone Well</div>
    <h1 class="headline">Building Soon?</h1>
    <p class="subhead">Start Here!</p>
    <p class="pack-title">Free Build Planning Pack:</p>

    <svg class="item-icon" style="top:209px" viewBox="0 0 16 16"><rect x="3" y="1" width="10" height="14" rx="1"/><line x1="5" y1="4" x2="11" y2="4"/><line x1="5" y1="8" x2="11" y2="8"/><line x1="5" y1="11" x2="11" y2="11"/></svg>
    <p class="pack-item" style="top:209px">Build Cost Calculator</p>
    <svg class="item-icon" style="top:237px" viewBox="0 0 16 16"><rect x="3" y="2" width="10" height="13" rx="1"/><rect x="6" y="1" width="4" height="2"/><polyline points="5.5,7 7,8.5 10,5.5"/><polyline points="5.5,11.5 7,13 10,10"/></svg>
    <p class="pack-item" style="top:237px">Hidden Cost Checklist</p>
    <svg class="item-icon" style="top:265px" viewBox="0 0 16 16"><line x1="8" y1="2" x2="8" y2="14"/><line x1="2" y1="4" x2="14" y2="4"/><path d="M1 10 L3.5 4 L6 10 Z"/><path d="M10 12 L12.5 6 L15 12 Z"/></svg>
    <p class="pack-item" style="top:265px">Builder Comparison<br>Guide</p>

    <p class="tagline">Build with confidence</p>
    <a class="cta">Download Now!</a>
    <div class="accent-bar"></div>
  </section>

  <section class="banner tall-ad" aria-label="Half page banner">
    <div class="photo" role="img" aria-label="Photo of a new two-storey house under construction with scaffolding and timber roof framing"></div>
    <div class="brand-mark"></div>
    <div class="brand-name">Stone Well</div>
    <h1 class="headline">Building Soon?</h1>
    <p class="subhead">Start Here!</p>
    <p class="pack-title">Free Build Planning Pack:</p>

    <svg class="item-icon" style="top:366px" viewBox="0 0 16 16"><rect x="3" y="1" width="10" height="14" rx="1"/><line x1="5" y1="4" x2="11" y2="4"/><line x1="5" y1="8" x2="11" y2="8"/><line x1="5" y1="11" x2="11" y2="11"/></svg>
    <p class="pack-item" style="top:366px">Build Cost Calculator</p>
    <svg class="item-icon" style="top:409px" viewBox="0 0 16 16"><rect x="3" y="2" width="10" height="13" rx="1"/><rect x="6" y="1" width="4" height="2"/><polyline points="5.5,7 7,8.5 10,5.5"/><polyline points="5.5,11.5 7,13 10,10"/></svg>
    <p class="pack-item" style="top:409px">Hidden Cost Checklist</p>
    <svg class="item-icon" style="top:453px" viewBox="0 0 16 16"><line x1="8" y1="2" x2="8" y2="14"/><line x1="2" y1="4" x2="14" y2="4"/><path d="M1 10 L3.5 4 L6 10 Z"/><path d="M10 12 L12.5 6 L15 12 Z"/></svg>
    <p class="pack-item" style="top:453px">Builder Comparison<br>Guide</p>

    <p class="tagline">Build with confidence</p>
    <a class="cta">Download Now!</a>
  </section>
</body>
</html>
```